Melvari Piano Studio Creative Card (EXISTING LOGO)

Hi all
We need an artistic, creative and modern business card design for our piano studio. Logo is attached, please let us know if you need other file formats.
The business card should convey high-end, prestigiousness, and be minimalist in feel. It should not look corporate or childish.
Rounded corners or creative shapes only, no regular square corners. Card should be double-sided. Can be portrait or landscape oriented. No preference to size either. Standard or custom size both okay.
We will not be giving out thousands of cards due to the nature of our business. We want to make sure that each business card we hand out, people will appreciate the design and printing quality that took place.
Please note, as the logo is supplied, we need more than just a layout with name and phone number etc inserted. Quite frankly,we can do that ourselves. We are interested in designs that has the different special printing methods in mind during the designing process. We are particularly interested in the effects of:
- Spot UV Varnish
- Foil
- Thermography
- Letterpress
- Die Cut
- Lamination
Colours does not have to be limited to black and white.
Information to be included:
Name (with qualification attached)
Mobile
website "melvari.com.au"
Designs submitted should include description of the printing method. The final format should be ready to be sent to printer with detailed printing method and colour (if applicable) instructions.
Much thanks in advance.
Updates
as per request from a designer, eps format file uploaded.

```html
<!DOCTYPE html>
<html lang="en">
<head>
<meta charset="utf-8">
<title>Melvari Piano Studio – Business Card</title>
<link href="https://fonts.googleapis.com/css2?family=Jost:wght@400;500&family=Open+Sans:wght@300;400;700&family=Courier+Prime&display=swap" rel="stylesheet">
<style>
  :root {
    --backdrop: #e4e0da;
    --card: #0a0a0a;
    --white: #ffffff;
    --text-light: #e6e6e6;
    --text-muted: #8c8c8c;
    --band-dark: #151515;
    --band-mid: #6e6e6e;
    --band-light: #a9a9a9;
    --band-edge: #d0d0d0;
  }
  * { margin: 0; padding: 0; box-sizing: border-box; }
  html, body { width: 1200px; height: 1123px; overflow: hidden; }
  body { background: var(--backdrop); position: relative; font-family: "Open Sans", sans-serif; }

  .card {
    position: absolute;
    width: 779px;
    background: var(--card);
    overflow: hidden;
    box-shadow: 0 6px 18px rgba(0,0,0,0.28);
  }
  .card--front { left: 85px; top: 78px; height: 445px; border-radius: 60px 0 60px 0; }
  .card--back  { left: 327px; top: 597px; height: 445px; border-radius: 0 60px 0 60px; }

  .brand { position: absolute; left: 143px; display: flex; align-items: center; gap: 40px; }
  .card--front .brand { top: 64px; }
  .card--back .brand { top: 135px; }
  .brand__square { width: 108px; height: 108px; background: var(--white); flex: none; }
  .brand__name {
    font-family: "Jost", sans-serif;
    font-weight: 400;
    color: var(--white);
    line-height: 1;
  }
  .brand__name-main { display: block; font-size: 60px; letter-spacing: 8px; }
  .brand__name-sub { display: block; font-size: 23px; letter-spacing: 15px; margin-top: 14px; }

  .band {
    position: absolute;
    left: 0; right: 0;
    height: 60px;
    border-top: 2px solid var(--band-edge);
    border-bottom: 2px solid var(--band-edge);
    background: linear-gradient(90deg,
      var(--band-mid) 0%, var(--band-dark) 18%, var(--band-mid) 32%,
      var(--band-light) 48%, var(--band-mid) 58%, var(--band-dark) 70%,
      var(--band-mid) 84%, var(--band-light) 100%);
    display: flex; align-items: center;
  }
  .card--front .band { top: 231px; padding-left: 236px; }
  .card--back .band { top: 310px; justify-content: center; }

  .holder__name { font-weight: 700; font-size: 25px; color: var(--white); letter-spacing: 0.3px; }
  .holder__role { font-weight: 400; font-size: 20px; color: var(--white); margin-left: 12px; }

  .contacts { position: absolute; top: 335px; left: 41px; right: 20px; font-size: 20px; font-weight: 300; line-height: 29px; }
  .contacts__col { position: absolute; top: 0; }
  .contacts__address { left: 0; color: var(--text-muted); font-size: 19px; }
  .contacts__phones { left: 262px; color: var(--text-light); }
  .contacts__online { left: 464px; color: var(--text-light); }
  .contact-line { display: flex; align-items: center; gap: 8px; white-space: nowrap; }
  .contact-line svg { width: 18px; height: 18px; flex: none; }

  .web {
    font-family: "Courier Prime", monospace;
    letter-spacing: 5px;
    font-size: 17px;
  }
  .card--front .web { position: absolute; top: 400px; left: 252px; color: var(--text-muted); }
  .card--back .web { color: #d0d0d0; font-size: 18px; }
</style>
</head>
<body>

<section class="card card--front" aria-label="Card front">
  <div class="brand">
    <div class="brand__square"></div>
    <div class="brand__name">
      <span class="brand__name-main">MELVARI</span>
      <span class="brand__name-sub">PIANO STUDIO</span>
    </div>
  </div>

  <div class="band">
    <span class="holder__name">ADRIAN KELLOW</span>
    <span class="holder__role">OWNER</span>
  </div>

  <div class="contacts">
    <div class="contacts__col contacts__address">
      <div>14 Harbour Rd Fitzroy</div>
      <div>VIC 3065 Australia</div>
    </div>
    <div class="contacts__col contacts__phones">
      <div class="contact-line">
        <svg viewBox="0 0 20 20" aria-hidden="true"><circle cx="10" cy="10" r="8.5" fill="none" stroke="#e6e6e6" stroke-width="1.4"/><path d="M7.3 5.5c-.8.6-1 1.9-.5 3.3.7 1.9 2.2 3.9 4 5 .9.5 1.8.5 2.4 0l.5-.6-1.8-1.6-.9.6c-.9-.5-1.8-1.7-2.2-2.7l.8-.8-1.1-2.2z" fill="#e6e6e6"/></svg>
        130 482 617
      </div>
      <div class="contact-line">
        <svg viewBox="0 0 20 20" aria-hidden="true"><rect x="5.5" y="4" width="9" height="15" rx="1.2" fill="none" stroke="#e6e6e6" stroke-width="1.4"/><rect x="7.5" y="6" width="5" height="4" fill="#e6e6e6"/><path d="M12.5 4V1" stroke="#e6e6e6" stroke-width="1.4"/><path d="M7.5 12h5M7.5 14h5M7.5 16h5" stroke="#e6e6e6" stroke-width="1"/></svg>
        0412 908 356
      </div>
    </div>
    <div class="contacts__col contacts__online">
      <div class="contact-line">
        <svg viewBox="0 0 20 20" aria-hidden="true"><rect x="6" y="3" width="8" height="5" fill="none" stroke="#e6e6e6" stroke-width="1.3"/><rect x="2.5" y="8" width="15" height="7" rx="1" fill="#e6e6e6"/><rect x="6" y="13" width="8" height="5" fill="#0a0a0a" stroke="#e6e6e6" stroke-width="1.3"/></svg>
        03 94 172 58
      </div>
      <div class="contact-line">
        <svg viewBox="0 0 20 20" aria-hidden="true"><circle cx="10" cy="10" r="3.2" fill="none" stroke="#e6e6e6" stroke-width="1.4"/><path d="M13.2 7v4.2c0 1.4 2.8 1.4 2.8-1.2A6 6 0 1 0 12.6 15.4" fill="none" stroke="#e6e6e6" stroke-width="1.4"/></svg>
        studio@melvari.com.au
      </div>
    </div>
  </div>

  <div class="web">www.melvari.com.au</div>
</section>

<section class="card card--back" aria-label="Card back">
  <div class="brand">
    <div class="brand__square"></div>
    <div class="brand__name">
      <span class="brand__name-main">MELVARI</span>
      <span class="brand__name-sub">PIANO STUDIO</span>
    </div>
  </div>

  <div class="band">
    <span class="web">www.melvari.com.au</span>
  </div>
</section>

</body>
</html>
```